lab equipment website

We need a fresh new look for a company website called quorvin. We will be using the current logo and brand colors on their current website quorvin.com. They want to keep their text and on-page SEO, but would like to reformat it to look more modern and fresh. They want to have everything be high performance with a great user experience. Their main call to action is for people to fill in a contact form so they can call them. There is some information that is purposely above the fold on the instrument pages. I will need the home page, about page and a leasing page.

```html
<!DOCTYPE html>
<html lang="en">
<head>
<meta charset="utf-8">
<title>quorvin — Lab Equipment Service Plans and Leasing</title>
<link href="https://fonts.googleapis.com/css2?family=Poppins:wght@300;400;500;600;700&display=swap" rel="stylesheet">
<style>
:root{
  --teal:#1dbf9f;
  --teal-deep:#12a092;
  --teal-dark:#0e8a80;
  --navy:#2e3842;
  --navy-soft:#3a4652;
  --ink:#3b3f45;
  --muted:#6d737a;
  --light:#f1f2f3;
  --white:#ffffff;
}
*{box-sizing:border-box;margin:0;padding:0}
html,body{width:1200px;height:3416px;overflow:hidden}
body{font-family:'Poppins',sans-serif;color:var(--ink);background:var(--white);position:relative}
a{color:inherit;text-decoration:none}
.section{position:absolute;left:0;width:1200px;overflow:hidden}

/* header */
.site-header{top:0;height:84px;background:var(--navy);display:flex;align-items:center;justify-content:space-between;padding:0 87px}
.brand{display:flex;align-items:center;gap:10px;color:var(--white)}
.brand-dot{width:22px;height:22px;border-radius:50%;background:var(--teal)}
.brand-name{font-weight:600;font-size:24px;color:var(--white)}
.main-nav{display:flex;gap:40px;font-size:14px;color:#d9dde1}
.main-nav a{padding-bottom:8px}
.main-nav a.active{color:var(--white);border-bottom:2px solid var(--teal)}

/* hero */
.hero{top:84px;height:469px;background:linear-gradient(180deg,#f5f5f6,#ebeced)}
.hero-copy{position:absolute;left:87px;top:110px;width:420px}
.hero-kicker{font-size:22px;font-weight:400;color:var(--ink)}
.hero-title{font-size:31px;font-weight:400;color:var(--ink);margin-top:2px}
.hero-title strong{color:var(--teal);font-weight:700;font-size:38px}
.hero-text{font-size:13px;line-height:22px;color:var(--muted);margin-top:18px;width:390px}
.link-more{display:inline-block;margin-top:28px;color:var(--teal);font-size:13px;font-weight:500;letter-spacing:1px}
.hero-visual{position:absolute;left:550px;top:70px;width:590px;height:280px;border-radius:6px;background:linear-gradient(135deg,#fbfbfc,#d9dde2)}

/* keep in touch */
.touch{top:553px;height:135px;background:var(--teal);color:var(--white)}
.touch-title{position:absolute;left:87px;top:22px;font-size:20px;font-weight:400}
.touch-field{position:absolute;top:70px;width:240px;border-bottom:1px solid rgba(255,255,255,.55);padding-bottom:8px;font-size:11px;letter-spacing:1px}
.touch-btn{position:absolute;left:877px;top:48px;width:236px;height:55px;background:var(--white);color:var(--teal);font-size:14px;font-weight:500;letter-spacing:1.5px;display:flex;align-items:center;justify-content:center}

/* features */
.features{top:688px;height:259px;background:var(--white);display:flex;padding:0 87px;align-items:center}
.feature{flex:1;text-align:center;padding:0 30px;border-right:1px solid #e2e4e6;height:160px}
.feature:last-child{border-right:none}
.feature-icon{width:58px;height:58px;margin:6px auto 22px;border-radius:10px;background:#e9ebed}
.feature-text{font-size:15px;line-height:22px;color:var(--ink);font-weight:500}

/* trust */
.trust{top:947px;height:469px}
.trust-photo{position:absolute;inset:0;background:linear-gradient(100deg,#c9ccd0 0%,#eceded 45%,#b8bcc1 100%)}
.trust-card{position:absolute;left:615px;top:73px;width:498px;height:323px;background:var(--white);padding:38px 40px}
.trust-title{font-size:25px;line-height:34px;font-weight:400;color:var(--teal)}
.trust-text{font-size:12.5px;line-height:22px;color:var(--muted);margin-top:22px}

/* needs & skills */
.needs{top:1416px;height:661px;background:linear-gradient(120deg,var(--teal) 0%,var(--teal-deep) 100%);color:var(--white)}
.needs-copy{position:absolute;left:87px;top:62px;width:555px}
.needs-title{font-size:25px;line-height:34px;font-weight:400}
.needs-text{font-size:12.5px;line-height:21px;margin-top:14px;color:rgba(255,255,255,.92)}
.check-list{list-style:none;margin-top:14px}
.check-list li{display:flex;align-items:flex-start;gap:14px;font-size:12.5px;line-height:20px;margin-bottom:13px}
.check-list svg{flex:none;margin-top:-2px}
.needs-text a{text-decoration:underline}
.skills{position:absolute;left:701px;top:62px;width:420px}
.skills-title{font-size:25px;font-weight:400;margin-bottom:22px}
.skills-title.second{margin-top:36px}
.ring-row{display:flex;gap:28px}
.ring{width:118px;text-align:center}
.ring-chart{position:relative;width:118px;height:118px}
.ring-chart span{position:absolute;inset:0;display:flex;align-items:center;justify-content:center;font-size:25px;font-weight:600}
.ring-label{font-size:14px;font-weight:600;line-height:19px;margin-top:12px}

/* testimonial */
.testimonial{top:2077px;height:576px;background:var(--white)}
.testimonial svg.waves{position:absolute;left:0;top:0}
.quote-card{position:absolute;left:405px;top:109px;width:390px;height:328px;background:var(--white);box-shadow:0 4px 18px rgba(0,0,0,.12);padding:50px 42px 0;text-align:center}
.quote-mark{position:absolute;font-size:54px;line-height:1;color:var(--teal);font-weight:700}
.quote-text{font-size:13px;line-height:23px;color:var(--ink)}
.quote-name{font-size:15px;font-weight:600;margin-top:14px}
.quote-role{font-size:10px;color:var(--muted)}
.avatar{position:absolute;left:566px;top:41px;width:68px;height:68px;border-radius:50%;background:linear-gradient(160deg,#c9a98a,#5a4a40);border:4px solid var(--white);box-shadow:0 2px 6px rgba(0,0,0,.15)}
.slider-nav{position:absolute;left:561px;top:470px;display:flex;gap:14px}
.slider-nav span{width:32px;height:32px;border-radius:50%;border:1.5px solid rgba(255,255,255,.85);display:flex;align-items:center;justify-content:center}

/* questions */
.questions{top:2653px;height:460px}
.questions-photo{position:absolute;inset:0;background:linear-gradient(90deg,#6f7275 0%,#8c8f92 50%,#a6a8aa 100%)}
.questions-copy{position:absolute;left:148px;top:88px;width:460px;color:var(--white)}
.questions-title{font-size:33px;font-weight:400}
.questions-text{font-size:15px;line-height:25px;margin-top:12px}
.phone-line{display:flex;align-items:center;gap:16px;margin-top:40px}
.phone-line strong{font-size:30px;font-weight:500}
.phone-line small{font-size:13px;align-self:flex-end;margin-bottom:6px}
.btn-teal{display:flex;align-items:center;justify-content:center;width:237px;height:57px;background:var(--teal);color:var(--white);font-size:14px;font-weight:500;letter-spacing:1.5px;margin-top:32px}

/* footer */
.site-footer{top:3113px;height:303px;background:var(--navy);color:#c9ced3}
.footer-about{position:absolute;left:87px;top:66px;width:345px}
.footer-about p{font-size:11.5px;line-height:17px;margin-top:20px}
.footer-divider{position:absolute;top:60px;width:1px;height:170px;background:rgba(255,255,255,.12)}
.footer-col{position:absolute;top:66px}
.footer-col h4{font-size:15px;font-weight:400;color:var(--white);margin-bottom:16px}
.link-list{list-style:none}
.link-list li{font-size:11.5px;line-height:22px;display:flex;align-items:center;gap:10px}
.link-list li::before{content:"";width:4px;height:4px;border-radius:50%;background:var(--teal)}
.contact-list{list-style:none}
.contact-list li{display:flex;gap:12px;font-size:11.5px;line-height:17px;margin-bottom:12px}
.contact-list strong{color:var(--white);font-weight:500}
.footer-bottom{position:absolute;left:87px;right:87px;top:240px;border-top:1px solid rgba(255,255,255,.12);display:flex;justify-content:space-between;align-items:center;padding-top:22px;font-size:11.5px}
.social{display:flex;gap:18px}
.social span{width:12px;height:12px;border-radius:50%;background:#d4d8dc}
</style>
</head>
<body>

<header class="section site-header">
  <a class="brand" href="#"><span class="brand-dot"></span><span class="brand-name">quorvin</span></a>
  <nav class="main-nav">
    <a class="active" href="#">Home</a><a href="#">About</a><a href="#">Leasing</a><a href="#">FAQs</a><a href="#">Contact</a>
  </nav>
</header>

<section class="section hero">
  <div class="hero-copy">
    <p class="hero-kicker">Our Goal is Simple:</p>
    <h1 class="hero-title"><strong>Save</strong> Labs Time &amp; Money</h1>
    <p class="hero-text">quorvin is a lab support program that provides scientists with comprehensive maintenance/repair coverage and operating lease solutions at an affordable price.</p>
    <a class="link-more" href="#">LEARN MORE &nbsp;›</a>
  </div>
  <div class="hero-visual" role="img" aria-label="Group of white laboratory instruments including an analyzer, a stacked chromatography system and a microscope"></div>
</section>

<section class="section touch">
  <h2 class="touch-title">Keep In Touch</h2>
  <div class="touch-field" style="left:87px">NAME*</div>
  <div class="touch-field" style="left:348px">PHONE</div>
  <div class="touch-field" style="left:610px">EMAIL*</div>
  <a class="touch-btn" href="#">CONTACT US</a>
</section>

<section class="section features">
  <div class="feature">
    <div class="feature-icon" role="img" aria-label="First aid kit icon"></div>
    <p class="feature-text">Worry Free Lab Equipment<br>PM/repair Coverage.</p>
  </div>
  <div class="feature">
    <div class="feature-icon" role="img" aria-label="Hand holding a coin icon"></div>
    <p class="feature-text">Cost-effective Lease<br>Structures and Payment<br>Plans.</p>
  </div>
  <div class="feature">
    <div class="feature-icon" role="img" aria-label="Microscope icon"></div>
    <p class="feature-text">Knowledge of The<br>Laboratory.</p>
  </div>
</section>

<section class="section trust">
  <div class="trust-photo" role="img" aria-label="Smiling businessman in a suit making an OK hand gesture in a bright office"></div>
  <div class="trust-card">
    <h2 class="trust-title">Trusted Company Offering Scientific Equipment Service Plans and Flexible Leases</h2>
    <p class="trust-text">At quorvin, our goal is to ensure the success of your business. Whether you are running a laboratory or other scientific facilities, we want to keep you provided with the best in cutting-edge equipment. That’s why we offer flexible scientific equipment leasing options with worry-free service plans to provide your business with the tools needed to perform at its peak.</p>
  </div>
</section>

<section class="section needs">
  <div class="needs-copy">
    <h2 class="needs-title">We Understand Your Needs Because<br>We are Scientists First</h2>
    <p class="needs-text">When it comes to creating innovative solutions that cater to your lab, quorvin’s dedicated team of problem-solvers has got you covered. Here’s how we save you time and money:</p>
    <ul class="check-list">
      <li><svg width="22" height="22" viewBox="0 0 22 22"><rect x="1" y="1" width="20" height="20" fill="none" stroke="#fff" stroke-width="1.5"/><path d="M5 11l4 4 8-9" fill="none" stroke="#fff" stroke-width="1.8"/></svg>We collaborate with you directly- no middlemen</li>
      <li><svg width="22" height="22" viewBox="0 0 22 22"><rect x="1" y="1" width="20" height="20" fill="none" stroke="#fff" stroke-width="1.5"/><path d="M5 11l4 4 8-9" fill="none" stroke="#fff" stroke-width="1.8"/></svg>We handle scientific equipment service, repairs, and maintenance</li>
      <li><svg width="22" height="22" viewBox="0 0 22 22"><rect x="1" y="1" width="20" height="20" fill="none" stroke="#fff" stroke-width="1.5"/><path d="M5 11l4 4 8-9" fill="none" stroke="#fff" stroke-width="1.8"/></svg>We consolidate and streamline the ancillary work associated with lab equipment procurement and service</li>
      <li><svg width="22" height="22" viewBox="0 0 22 22"><rect x="1" y="1" width="20" height="20" fill="none" stroke="#fff" stroke-width="1.5"/><path d="M5 11l4 4 8-9" fill="none" stroke="#fff" stroke-width="1.8"/></svg>We utilize our networks to bring you the most cost-savings possible</li>
      <li><svg width="22" height="22" viewBox="0 0 22 22"><rect x="1" y="1" width="20" height="20" fill="none" stroke="#fff" stroke-width="1.5"/><path d="M5 11l4 4 8-9" fill="none" stroke="#fff" stroke-width="1.8"/></svg>We improve cash flow by removing the upfront cost of purchasing, freeing up capital in your everyday budget</li>
      <li><svg width="22" height="22" viewBox="0 0 22 22"><rect x="1" y="1" width="20" height="20" fill="none" stroke="#fff" stroke-width="1.5"/><path d="M5 11l4 4 8-9" fill="none" stroke="#fff" stroke-width="1.8"/></svg>We may provide tax advantages with our lease structures</li>
    </ul>
    <p class="needs-text">We regularly provide businesses with what they need to improve their budget and efficiency. We offer <a href="#">laboratory equipment leasing</a> for a wide range of needs. If you want to discuss your needs more in-depth, don’t hesitate to call us at (415) 555-0148 or fill out our <a href="#">contact form</a>.</p>
  </div>

  <div class="skills">
    <h2 class="skills-title">Our Skills</h2>
    <div class="ring-row">
      <div class="ring">
        <div class="ring-chart"><svg width="118" height="118" viewBox="0 0 118 118"><circle cx="59" cy="59" r="52" fill="none" stroke="#2e3842" stroke-width="10"/><circle cx="59" cy="59" r="52" fill="none" stroke="#fff" stroke-width="10" stroke-dasharray="310.4 326.7" transform="rotate(-90 59 59)"/></svg><span>95%</span></div>
        <p class="ring-label">Cost Saving</p>
      </div>
      <div class="ring">
        <div class="ring-chart"><svg width="118" height="118" viewBox="0 0 118 118"><circle cx="59" cy="59" r="52" fill="none" stroke="#2e3842" stroke-width="10"/><circle cx="59" cy="59" r="52" fill="none" stroke="#fff" stroke-width="10" stroke-dasharray="294 326.7" transform="rotate(-90 59 59)"/></svg><span>90%</span></div>
        <p class="ring-label">Lease Plan<br>Flexibility</p>
      </div>
      <div class="ring">
        <div class="ring-chart"><svg width="118" height="118" viewBox="0 0 118 118"><circle cx="59" cy="59" r="52" fill="none" stroke="#fff" stroke-width="10"/></svg><span>100%</span></div>
        <p class="ring-label">Customer<br>Service</p>
      </div>
    </div>
    <h2 class="skills-title second">The Competition</h2>
    <div class="ring-row">
      <div class="ring">
        <div class="ring-chart"><svg width="118" height="118" viewBox="0 0 118 118"><circle cx="59" cy="59" r="52" fill="none" stroke="#fff" stroke-width="10"/><circle cx="59" cy="59" r="52" fill="none" stroke="#2e3842" stroke-width="10" stroke-dasharray="228.7 326.7" transform="rotate(18 59 59)"/></svg><span>30%</span></div>
        <p class="ring-label">Reliability</p>
      </div>
      <div class="ring">
        <div class="ring-chart"><svg width="118" height="118" viewBox="0 0 118 118"><circle cx="59" cy="59" r="52" fill="none" stroke="#2e3842" stroke-width="10"/><circle cx="59" cy="59" r="52" fill="none" stroke="#fff" stroke-width="10" stroke-dasharray="277.7 326.7" transform="rotate(-36 59 59)"/></svg><span>15%</span></div>
        <p class="ring-label">Continued<br>Support</p>
      </div>
    </div>
  </div>
</section>

<section class="section testimonial">
  <svg class="waves" width="1200" height="576" viewBox="0 0 1200 576">
    <path d="M0 190 C300 205 560 230 780 150 C940 90 1060 10 1200 0 V576 H0Z" fill="#2e3842"/>
    <path d="M0 212 C300 228 570 250 790 172 C950 112 1070 40 1200 32 V576 H0Z" fill="#17857c"/>
    <path d="M0 234 C300 250 580 270 800 196 C960 138 1080 72 1200 66 V576 H0Z" fill="#1dbf9f"/>
  </svg>
  <div class="avatar" role="img" aria-label="Portrait photo of the quoted team member"></div>
  <div class="quote-card">
    <span class="quote-mark" style="left:26px;top:34px">“</span>
    <p class="quote-text">My time spent in the lab opened my eyes to the passion and dedication that drives scientists, as well as the frustration of a tight budget and equipment upkeep. quorvin was created in order to help overcome these obstacles and enable scientists to focus on what they’re truly passionate about: research.</p>
    <span class="quote-mark" style="right:26px;top:240px">”</span>
    <p class="quote-name">Dana Reyes</p>
    <p class="quote-role">Lab Relations</p>
  </div>
  <div class="slider-nav">
    <span><svg width="10" height="12" viewBox="0 0 10 12"><path d="M7 1L2 6l5 5" fill="none" stroke="#fff" stroke-width="1.6"/></svg></span>
    <span><svg width="10" height="12" viewBox="0 0 10 12"><path d="M3 1l5 5-5 5" fill="none" stroke="#fff" stroke-width="1.6"/></svg></span>
  </div>
</section>

<section class="section questions">
  <div class="questions-photo" role="img" aria-label="Thoughtful businessman on a grey concrete wall with drawn question marks"></div>
  <div class="questions-copy">
    <h2 class="questions-title">Further questions?</h2>
    <p class="questions-text">Feel free to contact us if you have any questions or comments. We promise to get back to you within 24 hours.</p>
    <div class="phone-line">
      <svg width="38" height="38" viewBox="0 0 24 24"><path d="M6.6 2.5l3 3.4-1.9 2.3c1.2 2.6 3.4 4.8 6 6l2.3-1.9 3.4 3-1.6 3.2c-.4.7-1.2 1-2 .8C9.4 17.6 5.4 13.6 3.6 7.2c-.2-.8.1-1.6.8-2z" fill="none" stroke="#fff" stroke-width="1.4"/><path d="M14 3.5a7 7 0 0 1 6.5 6.5M14 6.5a4 4 0 0 1 3.5 3.5" fill="none" stroke="#fff" stroke-width="1.3"/></svg>
      <strong>(415) 555-0148</strong><small>or</small>
    </div>
    <a class="btn-teal" href="#">CONTACT US</a>
  </div>
</section>

<footer class="section site-footer">
  <div class="footer-about">
    <a class="brand" href="#"><span class="brand-dot"></span><span class="brand-name">quorvin</span></a>
    <p>We are a team of Bayview University scientists driven by our passion for research. We strive to serve the scientific community. We love what we do, and who we work with. Together we can make positive changes in the world of research.</p>
  </div>
  <span class="footer-divider" style="left:524px"></span>
  <div class="footer-col" style="left:631px">
    <h4>Quick Links</h4>
    <ul class="link-list"><li>Home</li><li>About</li><li>Leasing</li><li>FAQs</li><li>Contact</li></ul>
  </div>
  <span class="footer-divider" style="left:860px"></span>
  <div class="footer-col" style="left:943px">
    <h4>Contact Info</h4>
    <ul class="contact-list">
      <li><svg width="10" height="14" viewBox="0 0 10 14"><path d="M5 0a5 5 0 0 0-5 5c0 3.5 5 9 5 9s5-5.5 5-9a5 5 0 0 0-5-5zm0 7a2 2 0 1 1 0-4 2 2 0 0 1 0 4z" fill="#1dbf9f"/></svg><span><strong>Quorvin Inc.</strong><br>220 Harbor Lane, Suite 400<br>Oakland, CA 94607</span></li>
      <li><svg width="12" height="12" viewBox="0 0 24 24"><path d="M6.6 2.5l3 3.4-1.9 2.3c1.2 2.6 3.4 4.8 6 6l2.3-1.9 3.4 3-1.6 3.2c-.4.7-1.2 1-2 .8C9.4 17.6 5.4 13.6 3.6 7.2c-.2-.8.1-1.6.8-2z" fill="#1dbf9f"/></svg><span>(415) 555-0148</span></li>
      <li><svg width="12" height="10" viewBox="0 0 12 10"><rect x="0" y="0" width="12" height="10" rx="1" fill="#1dbf9f"/><path d="M0.5 1l5.5 4.5L11.5 1" fill="none" stroke="#2e3842" stroke-width="1"/></svg><span>info@quorvin.com</span></li>
    </ul>
  </div>
  <div class="footer-bottom">
    <span>Copyright © 2019. All Rights Reserved.</span>
    <div class="social" aria-label="Social links"><span></span><span></span><span></span><span></span></div>
  </div>
</footer>

</body>
</html>
```